Company Mission & Values Poster

I'd like an A2 Portrait Poster displaying our company's Mission & Values.
See our website for our logo, fonts, mission & values.
https://valtemo.com.au/

Our Mission: Creating homes for abundant life
Values: Love, Thinking, Team, Zoe.

Some ideas to consider:
Mission as the Headline then
A logo for each of the 4 Values and the words

Target Market(s)

Myself & my team

Industry/Entity Type

Real Estate

Font styles to use
Other font styles liked:
• Company fonts as seen on our website

```html
<!DOCTYPE html>
<html lang="en">
<head>
<meta charset="utf-8">
<title>Valtemo – Mission &amp; Values Poster</title>
<link rel="stylesheet" href="https://fonts.googleapis.com/css2?family=Playfair+Display:wght@700;800;900&family=Montserrat:wght@500;600&display=swap">
<style>
  :root {
    --ink-green: #0b3b31;
    --teal: #2c7a6a;
    --teal-light: #3a8b7a;
    --pill: #f1f2f2;
    --paper: #ffffff;
    --stage: #e8ecea;
    --charcoal: #1c1c1c;
    --map-grey: #d9dbdb;
  }
  * { box-sizing: border-box; margin: 0; padding: 0; }
  html, body { width: 1200px; height: 2400px; overflow: hidden; }
  body { background: var(--stage); position: relative; }

  .poster {
    position: absolute; left: 0; top: 351px;
    width: 1200px; height: 1697px;
    background: var(--paper);
    overflow: hidden;
  }
  .shapes { position: absolute; inset: 0; }

  .brand {
    position: absolute; left: 0; right: 0; top: 100px;
    display: flex; align-items: center; justify-content: center; gap: 44px;
  }
  .brand-dot {
    width: 96px; height: 96px; border-radius: 50%;
    background: var(--ink-green);
  }
  .brand-name {
    font-family: "Playfair Display", serif; font-weight: 700;
    font-size: 140px; line-height: 1; letter-spacing: 18px;
    color: var(--ink-green);
  }

  .world-map {
    position: absolute; left: 10px; top: 770px; width: 1180px; height: 900px;
    background: radial-gradient(ellipse at 50% 45%, rgba(200,203,203,.55), rgba(220,222,222,.25) 60%, rgba(255,255,255,0) 75%);
  }

  .mission-label {
    position: absolute; left: 40px; top: 468px; width: 235px;
    font-family: "Playfair Display", serif; font-weight: 900;
    color: var(--ink-green); text-align: center;
  }
  .mission-label .our { display: block; font-size: 104px; line-height: .9; }
  .mission-label .word { display: block; font-size: 46px; line-height: 1; letter-spacing: 1px; }

  .mission-copy { position: absolute; left: 428px; top: 415px; width: 720px; color: #fff; }
  .mission-title {
    font-family: "Playfair Display", serif; font-weight: 700;
    font-size: 62px; line-height: 62px; letter-spacing: 1px;
  }
  .mission-text {
    margin-top: 14px;
    font-family: "Montserrat", sans-serif; font-weight: 500;
    font-size: 24px; line-height: 29px;
  }

  .value {
    position: absolute; left: 40px; height: 144px;
    background: var(--pill); border-radius: 72px;
    box-shadow: 0 8px 10px rgba(0,0,0,.16), inset 0 0 0 2px #e6e7e7;
    display: flex; align-items: center;
  }
  .value-name {
    width: 263px; text-align: center;
    font-family: "Playfair Display", serif; font-weight: 700;
    font-size: 46px; color: var(--ink-green);
  }
  .value-name.teal { color: var(--teal); }
  .value-rule { width: 2px; height: 104px; background: #c9cccb; flex: none; }
  .value-text {
    padding-left: 16px;
    font-family: "Montserrat", sans-serif; font-weight: 500;
    font-size: 18px; line-height: 22px; color: var(--charcoal);
  }
  .value-love { top: 845px; width: 880px; }
  .value-love .value-text { width: 440px; }
  .value-thinking { top: 1034px; width: 780px; }
  .value-thinking .value-text { width: 418px; }
  .value-team { top: 1229px; width: 770px; }
  .value-team .value-text { width: 400px; }
  .value-zoe { top: 1424px; width: 880px; }
  .value-zoe .value-text { width: 420px; }

  .values-heading { position: absolute; inset: 0; }
</style>
</head>
<body>
<main class="poster">
  <div class="world-map" role="img" aria-label="Dotted world map background"></div>

  <svg class="shapes" width="1200" height="1697" viewBox="0 0 1200 1697" aria-hidden="true">
    <defs>
      <linearGradient id="bandGradient" x1="0" x2="1" y1="0" y2="0">
        <stop offset="0" stop-color="#0b3b31"/>
        <stop offset="1" stop-color="#2d7869"/>
      </linearGradient>
    </defs>
    <path d="M346,367 L1200,367 L1200,719 L346,719 A263,263 0 0 0 346,367 Z" fill="url(#bandGradient)"/>
    <path d="M43,306 A243,243 0 1 1 43,789" fill="none" stroke="var(--charcoal)" stroke-width="6"/>
    <path d="M144,341 A206,206 0 0 1 144,753" fill="none" stroke="var(--teal)" stroke-width="5"/>
    <circle cx="1116" cy="1231" r="369" fill="none" stroke="var(--charcoal)" stroke-width="6"/>
    <circle cx="1116" cy="1231" r="312" fill="none" stroke="var(--teal)" stroke-width="5" stroke-dasharray="120 60"/>
  </svg>

  <div class="brand">
    <span class="brand-dot"></span>
    <span class="brand-name">VALTEMO</span>
  </div>

  <h2 class="mission-label"><span class="our">OUR</span><span class="word">MISSION</span></h2>

  <section class="mission-copy">
    <h1 class="mission-title">CREATING HOMES<br>FOR ABUNDANT LIFE</h1>
    <p class="mission-text">We wholeheartedly believe that home is an extraordinary place: a haven where life unfolds in all its glory. Where we find solace, make cherished memories with loved ones, and savour the&nbsp; natural beauty that surrounds us.</p>
  </section>

  <div class="value value-love">
    <span class="value-name">Love</span><span class="value-rule"></span>
    <p class="value-text">Our mission is founded in our love and respect for people - those we develop for, those in our teams and those in the communities we create and operate within.</p>
  </div>
  <div class="value value-thinking">
    <span class="value-name teal">Thinking</span><span class="value-rule"></span>
    <p class="value-text">We believe in the power of thinking. Our rigorous and creative processes create beautifully considered solutions for our purchasers, the communities we develop within and the environment.</p>
  </div>
  <div class="value value-team">
    <span class="value-name">Team</span><span class="value-rule"></span>
    <p class="value-text">Property development is a team sport. We surround ourselves with the best designers and advisers. We strive to create an environment that allows them to do their best work and love doing it.</p>
  </div>
  <div class="value value-zoe">
    <span class="value-name teal">Zoe</span><span class="value-rule"></span>
    <p class="value-text">Our mission is to create places for ‘Zoe’ - the Greek word for abundant life. We do this through exquisite design, quality construction and celebrating nature.</p>
  </div>

  <svg class="values-heading" width="1200" height="1697" viewBox="0 0 1200 1697">
    <circle cx="923" cy="917" r="72" fill="var(--ink-green)" role="img" aria-label="Love icon: hugging heart"/>
    <circle cx="812" cy="1105" r="68" fill="var(--teal)" role="img" aria-label="Thinking icon: lightbulb brain"/>
    <circle cx="795" cy="1305" r="68" fill="var(--ink-green)" role="img" aria-label="Team icon: connected people"/>
    <circle cx="901" cy="1502" r="72" fill="var(--teal)" role="img" aria-label="Zoe icon: hands holding heart"/>
    <text transform="translate(996,1218) rotate(-90)" text-anchor="middle"
          font-family="'Playfair Display', serif" font-weight="900" font-size="105" fill="var(--ink-green)">OUR</text>
    <text transform="translate(1090,1226) rotate(-90)" text-anchor="middle"
          font-family="'Playfair Display', serif" font-weight="900" font-size="105" fill="var(--ink-green)">VALUES</text>
  </svg>
</main>
</body>
</html>
```